Presence Leadership Model

I am looking for a graphic design of the attached leadership model. The colors and design can be altered in any manner that brings the model alive version of the house model.

```html
<!DOCTYPE html>
<html lang="en">
<head>
<meta charset="UTF-8">
<title>Presence Leadership Model</title>
<link href="https://fonts.googleapis.com/css2?family=Carlito:wght@400;700&display=swap" rel="stylesheet">
<style>
  :root {
    --roof: #FFC000;
    --navy: #2F55A4;
    --org: #4472C4;
    --inter: #ED7D31;
    --personal: #70AD47;
    --wellbeing: #C00000;
    --band: #F2F2F2;
    --arrow: #E9EEF7;
    --ink: #111111;
    --white: #FFFFFF;
  }
  * { box-sizing: border-box; margin: 0; padding: 0; }
  html, body { width: 1200px; height: 675px; overflow: hidden; background: var(--white); }
  body { font-family: "Carlito", "Calibri", Arial, sans-serif; position: relative; }

  .roof { position: absolute; left: 0; top: 0; width: 1200px; height: 160px; }
  .roof-title {
    position: absolute; left: 0; width: 1200px; top: 64px; text-align: center;
    font-weight: 700; font-size: 24px; color: var(--navy); letter-spacing: 0.2px;
  }
  .roof-mission {
    position: absolute; left: 0; width: 1200px; top: 108px; text-align: center;
    font-weight: 700; font-size: 13.5px; line-height: 18px; color: var(--navy);
  }

  .band {
    position: absolute; left: 191px; width: 820px; background: var(--band);
    display: flex; align-items: center; justify-content: center;
    font-weight: 700; font-size: 14.5px; color: var(--ink);
    border-radius: 4px; box-shadow: 0 2px 4px rgba(0,0,0,0.08);
  }
  .band-outer { top: 173px; height: 32px; }
  .band-inner { top: 529px; height: 36px; }

  .flow-arrow { position: absolute; top: 322px; width: 80px; height: 90px; }
  .flow-arrow.one { left: 426px; }
  .flow-arrow.two { left: 728px; }

  .tile {
    position: absolute; color: var(--white); font-size: 12.5px; line-height: 16px;
    border-radius: 4px; display: flex; align-items: center;
    box-shadow: 0 2px 3px rgba(0,0,0,0.15);
  }
  .tile.head { flex-direction: column; justify-content: center; text-align: center; font-size: 12.5px; }
  .tile.head strong { font-weight: 700; }
  .org { background: var(--org); left: 191px; width: 212px; padding: 0 11px; }
  .org.head { left: 193px; }
  .inter { background: var(--inter); left: 495px; width: 212px; justify-content: center; text-align: center; padding: 0 10px; }
  .personal { background: var(--personal); left: 798px; width: 212px; padding: 0 11px; }

  .practice {
    position: absolute; height: 23px; width: 254px; background: var(--wellbeing); color: var(--white);
    display: flex; align-items: center; justify-content: center; font-size: 12px; letter-spacing: 0.3px;
    border-radius: 3px; box-shadow: 0 2px 3px rgba(0,0,0,0.15);
  }
  .col-a { left: 190px; } .col-b { left: 474px; } .col-c { left: 756px; }
  .row-1 { top: 577px; } .row-2 { top: 609px; }

  .base-line { position: absolute; left: 0; top: 668px; width: 1200px; height: 7px; background: var(--org); }
</style>
</head>
<body>
  <svg class="roof" viewBox="0 0 1200 160" aria-hidden="true">
    <polygon points="601,30 1010,148 199,148" fill="var(--roof)"/>
  </svg>
  <h1 class="roof-title">PRESENCE</h1>
  <p class="roof-mission">FOSTER CONTAGIOUS SUCCESS THROUGH PEOPLE,<br>RELATIONSHIPS AND A SHARED VISION</p>

  <div class="band band-outer">OUTER (IMPACT) STRATEGIES</div>

  <svg class="flow-arrow one" viewBox="0 0 80 90" aria-hidden="true">
    <polygon points="0,44 50,0 50,19 80,19 80,70 50,70 50,89" fill="var(--arrow)"/>
  </svg>
  <svg class="flow-arrow two" viewBox="0 0 80 90" aria-hidden="true">
    <polygon points="0,44 50,0 50,19 80,19 80,70 50,70 50,89" fill="var(--arrow)"/>
  </svg>

  <div class="tile org head" style="top:221px;height:41px;"><strong>ORGANIZATION LEVEL</strong><span>WINS THEORY</span></div>
  <div class="tile org" style="top:277px;height:44px;">Develop concrete outcomes, and visible results</div>
  <div class="tile org" style="top:340px;height:44px;">Foster in-depth changes, and new practices</div>
  <div class="tile org" style="top:402px;height:45px;">Have a micro, interpersonal or local impact</div>
  <div class="tile org" style="top:467px;height:44px;">Cultivate positive judgement, and shared ambition</div>

  <div class="tile inter head" style="top:221px;height:41px;"><strong>INTERPERSONAL LEVEL</strong><span>HEART LISTENING</span></div>
  <div class="tile inter" style="top:277px;height:35px;">Ask open-ended questions</div>
  <div class="tile inter" style="top:327px;height:35px;">Affirm someone’s strengths, efforts and past success</div>
  <div class="tile inter" style="top:376px;height:36px;">Reflect back what is shared for confirmation</div>
  <div class="tile inter" style="top:426px;height:36px;">Summarize key points to gain insights</div>
  <div class="tile inter" style="top:476px;height:35px;">Share and develop mutual expertise</div>

  <div class="tile personal head" style="top:221px;height:41px;"><strong>PERSONAL LEVEL</strong><span>INSIGHT DIALOGUE</span></div>
  <div class="tile personal" style="top:277px;height:32px;">Pause</div>
  <div class="tile personal" style="top:318px;height:32px;">Relax</div>
  <div class="tile personal" style="top:358px;height:32px;">Open</div>
  <div class="tile personal" style="top:399px;height:32px;">Attune to Emergence</div>
  <div class="tile personal" style="top:439px;height:32px;">Listen Deeply</div>
  <div class="tile personal" style="top:479px;height:32px;">Speak the Truth</div>

  <div class="band band-inner">INNER (WELLBEING) STRATEGIES</div>

  <div class="practice col-a row-1">PHYSICAL&nbsp; FITNESS</div>
  <div class="practice col-b row-1">HEART RATE VARIABILITY</div>
  <div class="practice col-c row-1">ISLAND HOPPIN CLUB</div>
  <div class="practice col-a row-2">NUTRITION</div>
  <div class="practice col-b row-2">NEUROFEEDBACK</div>
  <div class="practice col-c row-2">VIDEO GAMING CLUB</div>

  <div class="base-line"></div>
</body>
</html>
```